Business Card Design Project

Hello
I want a Simple Business card that uses the company logo that is easily reasonable but looks professional as I am an IT Services company and would look to share these cards with prospective clients.
The details are:
Kestrel Arc Solutions
14 Morrow Lane
Birmingham
B7 4QX
Telephone 0845 217 6640
I would like my name Oliver Hastings and my title Director on the card.
Target Market(s)
IT Professionals
Industry/Entity Type
Business

```html
<!DOCTYPE html>
<html lang="en">
<head>
<meta charset="utf-8">
<title>Kestrel Arc Solutions – Business Card</title>
<link rel="stylesheet" href="https://fonts.googleapis.com/css2?family=Lato:wght@400;700&display=swap">
<style>
  :root {
    --backdrop: #e9e9e7;
    --card-white: #ffffff;
    --ink: #1f1f1f;
    --logo-ink: #3b3839;
    --green-light: #b4d96e;
    --green-mid: #93c650;
    --green-deep: #5ea535;
    --mark-green: #9fd27a;
  }
  html, body {
    margin: 0;
    width: 1200px;
    height: 900px;
    overflow: hidden;
    background: var(--backdrop);
  }
  .business-card {
    position: absolute;
    left: 100px;
    top: 165px;
    width: 1000px;
    height: 570px;
    background: var(--card-white);
    box-shadow: 0 14px 34px rgba(0,0,0,0.18);
    overflow: hidden;
    font-family: "Lato", sans-serif;
  }
  .accent-field {
    position: absolute;
    left: 0;
    right: 0;
    top: 270px;
    bottom: 0;
    background: linear-gradient(160deg, var(--green-mid) 0%, var(--green-light) 40%, var(--green-deep) 100%);
  }
  .brand {
    position: absolute;
    left: 0;
    right: 0;
    top: 118px;
    display: flex;
    justify-content: center;
    align-items: center;
    gap: 16px;
  }
  .brand-dot {
    width: 34px;
    height: 34px;
    border-radius: 50%;
    background: var(--mark-green);
  }
  .brand-name {
    font-size: 46px;
    font-weight: 700;
    color: var(--logo-ink);
    letter-spacing: 0.5px;
  }
  .contact {
    position: absolute;
    left: 300px;
    width: 400px;
    top: 308px;
    text-align: center;
    color: var(--ink);
  }
  .contact-name {
    font-size: 30px;
    font-weight: 700;
    margin: 0;
  }
  .contact-title {
    font-size: 21px;
    margin: 2px 0 18px;
  }
  .contact-phone {
    font-size: 21px;
    margin: 0 0 14px;
  }
  .contact-address {
    font-size: 21px;
    font-style: normal;
    line-height: 1.3;
  }
</style>
</head>
<body>
  <div class="business-card">
    <div class="accent-field" role="img" aria-label="Decorative green curved band with coloured stripe"></div>

    <div class="brand">
      <span class="brand-dot"></span>
      <span class="brand-name">Kestrel Arc Solutions</span>
    </div>

    <div class="contact">
      <p class="contact-name">Oliver Hastings</p>
      <p class="contact-title">Director</p>
      <p class="contact-phone">0845 217 6640</p>
      <address class="contact-address">14 Morrow Lane<br>Birmingham, B7 4QX</address>
    </div>
  </div>
</body>
</html>
```